NimbusFern cyber security firm Website

We did our website ourselves on Joomla, it's not great. We want a wordpress based redesign. Some thing that will represent a modern cyber security firm that's aimed at solving business problems.
Https://nimbusfern.co.nz (current site)
#58427c - primary color (you'll know why when you see it's name)
Logo files can be provided. Ask for more info if you need.

We want a modern, quick to load website. Website is going to have a home - services - products - about us - blogs menu. Will need a footer menu, site map, contact page etc.
We getting Content done sperately.
Our logo is #58427c - so hoping for a light theme (or at least the top is).
While we have been specific around the color - we are not after a website that has too much of it.

Reference sites that we like :
https://www.voltaline.co.nz/ - Love the full screen real world image
https://wardvex.co.nz/ (love the real world imagry and motion)
https://www.qtr.com/us-en?lnk=m
https://redowlen.com

Please dont use :
cartoon or redered images : (Like this : https://img.stockmorra.com/free-vector/cyber-security-concept_23-2148543851.jpg?w=2000 )

Please don't use images like this : https://www.tavelundi.com/eu/blog/oil-gas/app/uploads/2020/04/116137226_s-1440x564_c.jpg - they are old and boring.

We would like to see some creativity - loading our logo into a readymade wordpress template and hitting go won't cut it.
Updates

Thanks everyone who has submitted so far. We've extended the deadline as we wanted to give everyone a chance to Re- read the brief and perhaps make some tweeks should they feel it necessary.

Target Market(s)

Mid - large enterprise, finance, insurance, utilities vertical

Industry/Entity Type

Cyber security

Coding

Coded - Design and coding required

Number of Pages Required

5+ page

Font styles to use
Other font styles liked:
• Open sans

Colors

Designer to choose colors to be used in the design.

Requirements
Must have
• Simple clear messaging, something that catches user engagement
Nice to have
• Motion of some sort, but not overdone, GDPR

```html
<!DOCTYPE html>
<html lang="en">
<head>
<meta charset="utf-8">
<title>NimbusFern — Cyber Security</title>
<link rel="stylesheet" href="https://fonts.googleapis.com/css2?family=Bebas+Neue&family=Open+Sans:wght@400;600&family=Poppins:wght@300;400;500;600&display=swap">
<style>
:root{
  --grape:#58427c;
  --grape-deep:#3d2a63;
  --grape-light:#7a5fa6;
  --navy:#0b1a3a;
  --navy-deep:#06112a;
  --ink:#222;
  --text:#3a3a3a;
  --muted:#8a8a8a;
  --white:#fff;
  --footer:#2e2e30;
  --line:#d9d4e3;
}
*{box-sizing:border-box;margin:0;padding:0}
html,body{width:1200px;height:4579px;overflow:hidden;background:var(--white)}
body{font-family:'Poppins',sans-serif;color:var(--text);position:relative}
.page{position:relative;width:1200px;height:4579px;overflow:hidden}
section,footer,header{position:absolute;left:0;width:1200px}
.abs{position:absolute}
.h2{font-family:'Open Sans',sans-serif;font-weight:400;color:var(--ink);font-size:42px;line-height:1.3;letter-spacing:.5px}
.rule{display:block;height:3px;background:var(--grape);width:44px;margin-top:6px}
.rule.dark{background:var(--ink);width:130px}
.btn{position:absolute;display:flex;align-items:center;justify-content:center;border-radius:18px;font-size:11px;font-family:'Poppins',sans-serif;height:28px;color:var(--white);background:var(--grape)}

/* hero */
.hero{top:0;height:590px;background:var(--white)}
.hero-curve{position:absolute;left:0;top:0}
.brand{position:absolute;left:28px;top:22px;display:flex;align-items:center;gap:8px;font-family:'Poppins',sans-serif;font-size:24px;font-weight:500;color:#222;letter-spacing:.5px}
.brand .dot{width:22px;height:22px;border-radius:50%;background:#222}
.nav{position:absolute;top:36px;left:655px;display:flex;gap:28px;font-size:14px;color:#eee}
.hero-art{position:absolute;left:22px;top:80px;width:470px;height:470px;border-radius:50%;background:radial-gradient(circle at 50% 45%,#8a3fb0 0%,#4a3160 40%,#1d1a24 70%,rgba(255,255,255,0) 71%)}
.hero-copy{position:absolute;left:686px;top:164px;color:var(--white)}
.hero-copy .kicker{font-family:'Bebas Neue',sans-serif;font-size:22px;letter-spacing:1px}
.hero-copy h1{font-family:'Bebas Neue',sans-serif;font-weight:400;font-size:96px;line-height:.95;letter-spacing:3px}
.hero-list{list-style:none;margin-top:22px;font-size:14px;line-height:27px}
.hero-list li::before{content:"";display:inline-block;width:6px;height:6px;border-radius:50%;background:#fff;margin-right:12px;vertical-align:middle}
.hero .btn-light{left:686px;top:444px;width:124px;background:#fff;color:var(--grape)}
.hero .btn-ghost{left:832px;top:444px;width:116px;background:transparent;border:1px solid #fff}

/* about */
.about{top:590px;height:500px}
.about .h2{position:absolute;left:88px;top:88px}
.about p{position:absolute;left:93px;top:158px;width:580px;font-size:14px;line-height:26px;color:#333}
.about .btn{left:88px;top:410px;width:124px}
.fern{position:absolute;left:795px;top:90px;width:330px;height:330px;background:linear-gradient(135deg,#e4e4e4,#a8a8a8);clip-path:polygon(92% 0,100% 6%,12% 100%,2% 94%)}

/* services */
.services{top:1090px;height:418px;background:radial-gradient(ellipse at 78% 45%,#1e3a70 0%,var(--navy) 45%,var(--navy-deep) 100%)}
.svc-card{position:absolute;width:110px;height:110px;border-radius:4px;display:flex;flex-direction:column;align-items:center;justify-content:center;gap:8px;font-size:11px;text-align:center;line-height:1.25}
.svc-card.light{background:#fff;color:#222}
.svc-card.dark{background:var(--grape);color:#fff}
.services .h2{position:absolute;left:588px;top:58px;color:#fff}
.services .rule{background:#fff;width:46px}
.services p{position:absolute;left:591px;top:144px;width:496px;font-size:14px;line-height:26px;color:#d7dcea}
.services .btn{left:588px;top:307px;width:124px}

/* third party */
.tprm{top:1508px;height:540px}
.tprm-img{position:absolute;left:52px;top:83px;width:530px;height:372px;background:linear-gradient(120deg,#f3a07a 0%,#8fb6e0 45%,#1c5aa0 100%)}
.tprm .h2{position:absolute;left:645px;top:80px;width:480px;line-height:1.2}
.tprm .rule{width:90px;background:var(--ink);height:2px}
.tprm p{position:absolute;left:645px;top:203px;width:520px;font-size:14px;line-height:22.5px;color:#333}
.tprm .btn{left:645px;top:424px;width:124px;background:#111}

/* what we do */
.what{top:2047px;height:502px;background:linear-gradient(90deg,#3b2a66 0%,#4a3a7e 45%,#4e4c86 70%,#37385f 100%)}
.what-photo{position:absolute;left:600px;top:0;width:600px;height:502px;background:radial-gradient(ellipse at 55% 45%,rgba(120,110,170,.55),rgba(40,40,80,0) 70%)}
.what .h2{position:absolute;left:55px;top:48px;color:#fff;line-height:1.35}
.what .rule{background:#fff;width:90px;height:2px}
.what p{position:absolute;left:55px;width:520px;font-size:12.5px;line-height:20px;color:#e9e6f2}
.what .btn{left:55px;top:420px;width:124px;background:var(--grape-light)}

/* trusted */
.trusted{top:2549px;height:316px}
.trusted .title{position:absolute;left:0;width:1200px;top:42px;text-align:center}
.trusted .rule{margin:4px auto 0;width:128px;background:#111}
.clients{position:absolute;top:150px;left:30px;width:1140px;display:flex;justify-content:space-between;align-items:center}
.client{width:170px;text-align:center;font-family:'Open Sans',sans-serif;font-size:30px;font-weight:600;color:#555;display:flex;align-items:center;justify-content:center;gap:8px}
.client .mk{width:14px;height:14px;background:#999}
.dots{position:absolute;top:258px;left:566px;display:flex;gap:7px}
.dots span{width:7px;height:7px;border-radius:50%;background:var(--grape)}

/* award */
.award{top:2865px;height:265px;background:linear-gradient(90deg,#2a1d55 0%,#3d2a7a 45%,#6a3fc0 70%,#3a2a80 100%)}
.award .left{position:absolute;left:12px;top:150px;color:#fff;font-family:'Bebas Neue',sans-serif;font-size:40px;letter-spacing:3px;line-height:1}
.award .left small{display:block;font-size:40px;letter-spacing:1px;margin-left:355px}
.award .big{position:absolute;left:662px;top:60px;color:#fff;font-family:'Poppins',sans-serif;font-weight:400;font-size:128px;line-height:1;letter-spacing:2px}
.award .burst{position:absolute;left:490px;top:50px;width:150px;height:150px;border-radius:50%;background:radial-gradient(circle,rgba(255,255,255,.55),rgba(255,255,255,0) 70%)}
.award .base{position:absolute;left:0;bottom:0;width:1200px;height:4px;background:linear-gradient(90deg,#e0446a,#6a3fc0)}

/* blogs */
.blogs{top:3130px;height:630px}
.blogs .title{position:absolute;top:62px;width:1200px;text-align:center}
.blogs .rule{margin:4px auto 0;width:130px;background:#111}
.post{position:absolute;top:170px;width:330px}
.post .img{height:240px}
.post p{margin-top:22px;font-size:13px;line-height:17px;color:#444;padding:0 12px}
.post .more{margin:22px 0 0 12px;width:158px;height:38px;border:1px solid #333;border-radius:20px;display:flex;align-items:center;justify-content:center;font-size:13px;color:#222}

/* contact */
.contact{top:3760px;height:512px}
.contact .h2{position:absolute;left:100px;top:86px}
.contact .rule{width:90px;background:#111;height:2px}
.contact .lead{position:absolute;left:103px;top:190px;width:440px;font-size:13px;line-height:21px;color:var(--muted)}
.contact-list{position:absolute;left:105px;top:292px;list-style:none;font-size:14px;color:#666}
.contact-list li{display:flex;align-items:center;gap:18px;height:52px}
.form{position:absolute;left:697px;top:38px;width:367px;height:412px;background:#fff;box-shadow:0 2px 18px rgba(0,0,0,.14)}
.form h3{position:absolute;left:36px;top:30px;font-family:'Open Sans',sans-serif;font-weight:600;font-size:18px;color:var(--grape);letter-spacing:.5px}
.field{position:absolute;left:36px;width:290px;border:1px solid #999;border-radius:3px;font-size:10px;color:#999;padding:7px 14px;height:34px}
.form .btn{left:40px;top:341px;width:286px;height:34px;font-size:14px}

/* footer */
.footer{top:4272px;height:307px;background:var(--footer);color:#fff}
.fbrand{position:absolute;left:92px;top:80px;display:flex;align-items:center;gap:10px;font-size:26px;font-weight:500}
.fbrand .dot{width:26px;height:26px;border-radius:50%;background:#fff}
.footer .about-txt{position:absolute;left:96px;top:138px;width:290px;font-size:11px;line-height:21px;color:#ddd}
.fcol h4{font-family:'Poppins',sans-serif;font-weight:600;font-size:19px;letter-spacing:.5px}
.fcol{position:absolute;top:80px}
.links{list-style:none;margin-top:16px;margin-left:7px;font-size:10.5px;line-height:14.5px}
.fcontact{list-style:none;margin-top:18px;font-size:14px;line-height:20px}
.fcontact li{display:flex;gap:14px;margin-bottom:10px}
.social{display:flex;gap:20px;margin-top:20px}
.social span{width:16px;height:16px;border-radius:50%;background:#fff}
.footer .copy{position:absolute;left:0;top:280px;width:1200px;text-align:center;font-size:10px;color:#ccc;border-top:1px solid #666;padding-top:8px;margin-left:0}
</style>
</head>
<body>
<div class="page">

<header class="hero">
  <svg class="hero-curve" width="1200" height="590" viewBox="0 0 1200 590">
    <defs><linearGradient id="heroGrad" x1="0" y1="0" x2="1" y2="1"><stop offset="0" stop-color="#8466b8"/><stop offset="1" stop-color="#5a3f86"/></linearGradient></defs>
    <path d="M640 0 H1200 V590 H310 C520 500 660 300 640 0 Z" fill="url(#heroGrad)"/>
    <path d="M700 0 C720 260 600 470 420 590" stroke="rgba(255,255,255,.08)" stroke-width="40" fill="none"/>
    <path d="M790 0 C810 280 700 480 540 590" stroke="rgba(255,255,255,.06)" stroke-width="40" fill="none"/>
  </svg>
  <div class="brand"><span class="dot"></span>NIMBUSFERN</div>
  <div class="hero-art" role="img" aria-label="Large dark emblem filled with purple network imagery"></div>
  <nav class="nav"><span>Home</span><span>Services</span><span>Products</span><span>Who We Are</span><span>About us</span><span>blogs</span></nav>
  <div class="hero-copy">
    <div class="kicker">Welcome to</div>
    <h1>Nimbus Fern</h1>
    <ul class="hero-list"><li>Human Risk Management</li><li>Quantify Risk</li><li>Security at the edge</li><li>Cloud Security</li></ul>
  </div>
  <div class="btn btn-light">Get In Touch</div>
  <div class="btn btn-ghost">View more</div>
</header>

<section class="about">
  <h2 class="h2">NimbusFern<span class="rule"></span></h2>
  <p>NimbusFern is a 100% New Zealand owned and operated cyber security company, providing cyber risk mitigation and management solutions to all businesses. We pride ourselves in delivering enterprise grade security solutions, to businesses of all sizes and industries, in Aotearoa.Being 'purple' we focus on both Blue and Red team security solutions, assisting our clients in implementing new security controls, as well as testing the ones they already have.<br>Our key value is integrity, and we believe in being fully transparent when working with our clients and partners to ensure we achieve the best possible security solutions for the best price.</p>
  <div class="btn">Get Started</div>
  <div class="fern" role="img" aria-label="Grey silver fern frond"></div>
</section>

<section class="services">
  <div class="svc-card light" style="left:126px;top:88px">
    <svg width="44" height="40" viewBox="0 0 44 40" fill="none" stroke="#222" stroke-width="2"><rect x="6" y="4" width="32" height="20" rx="4"/><circle cx="14" cy="14" r="2"/><circle cx="22" cy="14" r="2"/><circle cx="30" cy="14" r="2"/><circle cx="16" cy="32" r="5"/><path d="M21 32h16M32 32v4"/></svg>
    <span>Password<br>Management</span></div>
  <div class="svc-card dark" style="left:259px;top:88px">
    <svg width="48" height="48" viewBox="0 0 48 48" fill="none" stroke="#fff" stroke-width="2"><circle cx="24" cy="24" r="18"/><path d="M24 12l9 4v8c0 6-4 10-9 12-5-2-9-6-9-12v-8z"/><path d="M20 24l3 3 5-6"/></svg>
    <span>virtual CISO</span></div>
  <div class="svc-card dark" style="left:156px;top:222px">
    <svg width="48" height="44" viewBox="0 0 48 44" fill="none" stroke="#fff" stroke-width="2"><circle cx="18" cy="18" r="11"/><circle cx="14" cy="17" r="2"/><circle cx="22" cy="17" r="2"/><path d="M32 8h10M32 14h12M30 30h14M4 36h20"/></svg>
    <span>Cyber Threat</span></div>
  <div class="svc-card light" style="left:288px;top:222px">
    <svg width="40" height="46" viewBox="0 0 40 46" fill="none" stroke="#222" stroke-width="2"><circle cx="20" cy="10" r="6"/><path d="M8 42V28c0-5 5-9 12-9s12 4 12 9v14"/><circle cx="32" cy="14" r="4"/></svg>
    <span>Human Risk<br>Management</span></div>
  <h2 class="h2">Services<span class="rule"></span></h2>
  <p>Lorem ipsum dolor sit amet consectetur. Ac nunc et urna tempor urna amet neque diam id. Urna a ac sed urna non in massa ut. Sem ut donec id ipsum at. Ipsum quisque id fermentum quam ut amet. Purus consequat ac massa in proin nisl tortor. Egestas adipiscing cursus felis eget porttitor commodo cursus tellus purus.</p>
  <div class="btn">Get Started</div>
</section>

<section class="tprm">
  <div class="tprm-img" role="img" aria-label="Photo of hands typing on a laptop with glowing padlock icons"></div>
  <h2 class="h2">Third-Party Risk Management<span class="rule"></span></h2>
  <p>The Redowlen Solution provides a technical cyber rating following and applying commonly-used frameworks developed by the Varnholt Corporation for scoring software weaknesses in a consistent, flexible, and transparent manner, converting highly technical terms into simple letter grades While other security ratings service (SRS) providers try to narrow the scope, Redowlen provides the only standards-based cyber risk assessments that analyse your supply chain's cybersecurity posture from three critical dimensions together: technical, financial, and compliance.</p>
  <div class="btn">Get Started</div>
</section>

<section class="what">
  <div class="what-photo" role="img" aria-label="Photo of a thoughtful man in glasses and a waistcoat"></div>
  <h2 class="h2">What We do, and<br>how we do it<span class="rule"></span></h2>
  <p style="top:186px">We believe that third party risk management has historically been an "enterprise" activity, and the costs of performing an effective Cyber Risk review on a business partner or service provider has simply been expensive, requiring specialised skill sets that are difficult to find and retain.</p>
  <p style="top:286px">NimbusFern's view is that we can help our clients of any size. All companies have a need for third-party cyber security risk management – its not just for the "big companies" We believe all organisations want to have intelligence reporting on themselves, so that they best mitigate cyber security issues before it affects their operations.</p>
  <div class="btn">Learn More</div>
</section>

<section class="trusted">
  <div class="title"><h2 class="h2">Trusted By<span class="rule"></span></h2></div>
  <div class="clients">
    <div class="client">Quorra</div>
    <div class="client" style="font-size:20px"><span class="mk"></span>Halden Trust</div>
    <div class="client">QTR</div>
    <div class="client">Vexa</div>
    <div class="client" style="font-size:24px"><span class="mk"></span>Brindle</div>
    <div class="client" style="font-size:22px">Certivo</div>
  </div>
  <div class="dots"><span></span><span></span><span></span><span></span><span></span></div>
</section>

<section class="award">
  <div class="burst" role="img" aria-label="Dotted light burst"></div>
  <div class="left">CHANNELWIRE INNOVATION<small>AWARDS 2022</small></div>
  <div class="big">FINALIST</div>
  <div class="base"></div>
</section>

<section class="blogs">
  <div class="title"><h2 class="h2">Blogs/News<span class="rule"></span></h2></div>
  <article class="post" style="left:67px">
    <div class="img" role="img" aria-label="Photo of an open red padlock over binary code" style="background:linear-gradient(135deg,#a9c3e6,#33558a 70%,#7a1c22)"></div>
    <p>Lorem ipsum dolor sit amet, consectetur adipiscing elit. Nibh odio aliquet vel id quis orci, diam mi, in. Eleifend quam id gravida urna, a sed. Blandit tellus amet felis sit congue.</p>
    <div class="more">LEARN MORE ››</div>
  </article>
  <article class="post" style="left:432px">
    <div class="img" role="img" aria-label="Photo of a red padlock on a green lit keyboard" style="background:linear-gradient(135deg,#0c2a12,#1f7a2c 55%,#b52a1f)"></div>
    <p>Lorem ipsum dolor sit amet, consectetur adipiscing elit. Nibh odio aliquet vel id quis orci, diam mi, in. Eleifend quam id gravida urna, a sed. Blandit tellus amet felis sit congue.</p>
    <div class="more">LEARN MORE ››</div>
  </article>
  <article class="post" style="left:797px">
    <div class="img" role="img" aria-label="Photo of a pole with many security cameras" style="background:linear-gradient(160deg,#f2f2f2,#c7ccd2 60%,#3a3d42)"></div>
    <p>Lorem ipsum dolor sit amet, consectetur adipiscing elit. Nibh odio aliquet vel id quis orci, diam mi, in. Eleifend quam id gravida urna, a sed. Blandit tellus amet felis sit congue.</p>
    <div class="more">LEARN MORE ››</div>
  </article>
</section>

<section class="contact">
  <h2 class="h2">Get In Touch<span class="rule"></span></h2>
  <p class="lead">Lorem ipsum dolor sit amet, consectetur adipiscing elit. A a feugiat nisl velit mauris sed arcu nunc ullamcorper.</p>
  <ul class="contact-list">
    <li><svg width="18" height="18" viewBox="0 0 24 24" fill="#58427c"><path d="M6 2l4 4-2 3c1 3 4 6 7 7l3-2 4 4-3 4C10 22 2 14 2 5z"/></svg>+64 (0) 210 555 0142</li>
    <li><svg width="20" height="16" viewBox="0 0 24 18" fill="none" stroke="#58427c" stroke-width="2"><rect x="1" y="1" width="22" height="16"/><path d="M1 1l11 9 11-9"/></svg>www.mail.nimbusfern.co.nz</li>
    <li><svg width="18" height="18" viewBox="0 0 24 24" fill="#58427c"><path d="M22 2L2 10l9 3 3 9z"/></svg>42b Kereru Lane, Tawhiti, New Plymouth, 4381</li>
    <li><svg width="20" height="20" viewBox="0 0 24 24" fill="none" stroke="#58427c" stroke-width="2"><circle cx="12" cy="12" r="10"/><path d="M12 6v6l4 3"/></svg>Mon – Fri 8am – 5pm</li>
  </ul>
  <div class="form">
    <h3>SAY SOMETHING</h3>
    <div class="field" style="top:74px">Your Name</div>
    <div class="field" style="top:130px">Your Email</div>
    <div class="field" style="top:190px;height:118px">Your Message</div>
    <div class="btn">Send</div>
  </div>
</section>

<footer class="footer">
  <div class="fbrand"><span class="dot"></span>NIMBUSFERN</div>
  <p class="about-txt">NimbusFern is a 100% New Zealand owned and operated cyber security company, providing cyber risk mitigation and management solutions to all businesses.</p>
  <div class="fcol" style="left:418px"><h4>QUICK LINKS</h4>
    <ul class="links"><li>Home</li><li>Services</li><li>Products</li><li>About Us</li><li>Blogs</li><li>Site Map</li></ul></div>
  <div class="fcol" style="left:620px"><h4>CONTACT US</h4>
    <ul class="fcontact"><li><span>☎</span>+64 (0) 210 555 0142</li><li><span>✉</span>www.mail.nimbusfern.co.nz</li><li><span>➤</span>42b Kereru Lane, Tawhiti,<br>New Plymouth, 4381</li></ul></div>
  <div class="fcol" style="left:928px"><h4>FOLLOW US</h4>
    <div class="social"><span></span><span></span><span></span><span></span></div></div>
  <div class="copy">© copyright 2021 All Right Reserved NimbusFern</div>
</footer>

</div>
</body>
</html>
```